Business Card for Dental Office

I need a business card that reflects a modern day dental office, called Heron Creek Dental. We specialize in general and Cosmetic Dentistry. On the front it must have the business information and the logo and the back side QR code and a place to note the appointment. I have attached the logo and a current business card for the information

Target Market(s)

Patients with Dental care need

Industry/Entity Type

Health Care

Contact Information for Business Card

Regular size business card with round corners

Font styles to use
Other font styles liked:
• lato light font

Colors
34a7d8
0255a3
ffffff
000000
85cae6
85acd3

Requirements
Must have
• The logo, business information, website and in the a place to write down the appointment
Nice to have
• QR Code in the back

```html
<!DOCTYPE html>
<html lang="en">
<head>
<meta charset="utf-8">
<title>Heron Creek Dental – Business Card</title>
<link rel="stylesheet" href="https://fonts.googleapis.com/css2?family=Lato:ital,wght@0,300;0,400;0,700;1,100;1,300&display=swap">
<style>
  :root {
    --brand-navy: #0255a3;
    --brand-sky: #34a7d8;
    --brand-mist: #85cae6;
    --card-bg: #fafcfe;
    --page-bg: #ffffff;
  }
  html, body {
    margin: 0;
    padding: 0;
    width: 1200px;
    height: 666px;
    overflow: hidden;
    background: var(--page-bg);
  }
  .card {
    position: relative;
    width: 1200px;
    height: 666px;
    background: var(--card-bg);
    border-radius: 22px;
    overflow: hidden;
    font-family: "Lato", Arial, sans-serif;
    color: var(--brand-navy);
  }
  .brand-mark {
    position: absolute;
    left: 524px;
    top: 58px;
    width: 140px;
    height: 140px;
    border-radius: 50%;
    background: var(--brand-sky);
  }
  .brand-name {
    position: absolute;
    left: 0;
    width: 1188px;
    top: 244px;
    margin: 0;
    text-align: center;
    font-weight: 400;
    font-size: 47px;
    line-height: 1;
    color: var(--brand-navy);
  }
  .dentist-name {
    position: absolute;
    left: 0;
    width: 1192px;
    top: 368px;
    margin: 0;
    text-align: center;
    font-weight: 700;
    font-size: 50px;
    line-height: 1;
    letter-spacing: 0.2px;
  }
  .specialty {
    position: absolute;
    left: 0;
    width: 1192px;
    top: 432px;
    margin: 0;
    text-align: center;
    font-weight: 100;
    font-style: italic;
    font-size: 50px;
    line-height: 1;
    color: var(--brand-navy);
  }
  .divider {
    position: absolute;
    left: 30px;
    top: 561px;
    width: 1138px;
    height: 2px;
    background: linear-gradient(90deg, var(--brand-navy), var(--brand-sky) 50%, var(--brand-navy));
  }
  .contact {
    position: absolute;
    top: 572px;
    font-weight: 300;
    font-size: 40px;
    line-height: 45px;
    white-space: nowrap;
  }
  .contact p { margin: 0; }
  .address { left: 28px; }
  .phones {
    right: 32px;
    text-align: right;
  }
  .phone-line {
    display: flex;
    justify-content: flex-end;
    align-items: center;
  }
  .icon {
    width: 34px;
    height: 34px;
    margin-right: 4px;
    flex: none;
  }
  .fax-icon { margin-left: 20px; }
</style>
</head>
<body>
  <div class="card">
    <div class="brand-mark" aria-hidden="true"></div>
    <h1 class="brand-name">Heron Creek Dental</h1>

    <h2 class="dentist-name">Marin Okafor, D.M.D.</h2>
    <p class="specialty">General &amp; Cosmetic Dentistry</p>

    <div class="divider"></div>

    <div class="contact address">
      <p>2618 Alder Grove Ave.</p>
      <p>Fairview CA 90311</p>
    </div>

    <div class="contact phones">
      <div class="phone-line">
        <svg class="icon" viewBox="0 0 34 34" aria-label="Phone">
          <rect width="34" height="34" rx="6" fill="var(--brand-navy)"/>
          <path d="M10 7.5c1-.6 2-.4 2.6.5l2.3 3.6c.5.8.3 1.8-.4 2.4l-1.5 1.2c1 2.4 2.8 4.3 5.2 5.4l1.3-1.5c.6-.7 1.6-.8 2.4-.3l3.6 2.3c.9.6 1.1 1.7.5 2.6l-1.2 1.8c-.8 1.2-2.3 1.7-3.6 1.2C14.6 24.6 9.4 19.4 7.3 13c-.4-1.3.1-2.7 1.2-3.5z" fill="#ffffff"/>
        </svg>
        <span>555.204.7318</span>
        <svg class="icon fax-icon" viewBox="0 0 34 34" aria-label="Fax">
          <rect x="1.5" y="6" width="31" height="26" rx="5" fill="none" stroke="var(--brand-navy)" stroke-width="3"/>
          <rect x="5" y="9" width="7" height="20" rx="2" fill="var(--brand-navy)"/>
          <rect x="14" y="2" width="15" height="10" fill="var(--card-bg)" stroke="var(--brand-navy)" stroke-width="2.5"/>
          <g fill="var(--brand-navy)">
            <rect x="15" y="15" width="3" height="3"/><rect x="20" y="15" width="3" height="3"/><rect x="25" y="15" width="3" height="3"/>
            <rect x="15" y="20" width="3" height="3"/><rect x="20" y="20" width="3" height="3"/><rect x="25" y="20" width="3" height="3"/>
            <rect x="15" y="25" width="3" height="3"/><rect x="20" y="25" width="3" height="3"/><rect x="25" y="25" width="3" height="3"/>
          </g>
        </svg>
        <span>555.204.7390</span>
      </div>
      <p>www.heroncreekdental.com</p>
    </div>
  </div>
</body>
</html>
```